BKT Consulting

Government/Entitlement Consulting Services- I assist developers obtain entitlements from local, state and federal government agencies so that they can build their projects. Often these projects are very complicated and political and may face community opposition.

Target Market(s)

Real Estate Developers

Industry/Entity Type

Business Consultant

Contact Information for Business Card

Dana Velmonte
Principal

Font styles to use
Serif
Sans Serif

Requirements
Must have
• Classy and professional appeal.
Nice to have
• I like a combination of a mat and glossy finish. I've seen that done with black and then a bold color for a pop, but am not 100% committed to that.

```html
<!DOCTYPE html>
<html lang="en">
<head>
<meta charset="utf-8">
<title>BKT Consulting – Business Card</title>
<link rel="stylesheet" href="https://fonts.googleapis.com/css2?family=Tinos:wght@400;700&family=Arimo&family=Cinzel:wght@600&display=swap">
<style>
  :root {
    --backdrop: #2b2b2b;
    --card: #000000;
    --ink: #ffffff;
    --accent: #e8622a;
    --rule: #cfcfcf;
  }
  * { margin: 0; padding: 0; box-sizing: border-box; }
  html, body { width: 1200px; height: 900px; overflow: hidden; }
  body { background: var(--backdrop); position: relative; color: var(--ink); }

  .card {
    position: absolute;
    background: var(--card);
    box-shadow: 0 10px 22px rgba(0,0,0,0.55);
  }
  .card-front { left: 280px; top: 66px; width: 617px; height: 370px; }
  .card-back  { left: 283px; top: 470px; width: 619px; height: 370px; }

  /* Front: brand block */
  .front-brand {
    position: absolute; left: 92px; top: 112px; width: 194px;
    display: flex; flex-direction: column; align-items: center;
  }
  .front-brand-circle {
    width: 104px; height: 104px;
    border: 2px solid var(--accent); border-radius: 50%;
  }
  .front-brand-name {
    margin-top: 14px;
    font-family: "Tinos", serif; font-weight: 400; font-size: 22px;
    color: var(--ink); white-space: nowrap;
  }
  .divider {
    position: absolute; left: 306px; top: 132px;
    width: 1.5px; height: 106px; background: var(--rule);
  }
  .contact { position: absolute; left: 340px; top: 130px; }
  .contact-name {
    font-family: "Tinos", serif; font-weight: 400; font-size: 24px; line-height: 1;
  }
  .contact-title {
    font-family: "Tinos", serif; font-weight: 700; font-size: 14px; color: var(--accent);
    margin-top: 5px;
  }
  .contact-lines {
    list-style: none; margin-top: 9px;
    font-family: "Arimo", sans-serif; font-size: 14.5px; line-height: 20.5px;
  }
  .contact-lines li { padding-left: 23px; position: relative; white-space: nowrap; }
  .contact-lines svg { position: absolute; left: 0; top: 5px; }
  .address {
    position: absolute; left: 0; right: 0; top: 307px;
    text-align: center;
    font-family: "Arimo", sans-serif; font-size: 14px;
  }

  /* Back */
  .back-circle {
    position: absolute; left: 241px; top: 90px;
    width: 134px; height: 134px;
    border: 2px solid var(--ink); border-radius: 50%;
  }
  .brand-name {
    position: absolute; left: 0; right: 0; top: 232px;
    text-align: center;
    font-family: "Cinzel", serif; font-weight: 600; font-size: 33px;
    letter-spacing: 1px;
  }
  .tagline {
    position: absolute; left: 0; right: 0; top: 273px;
    text-align: center;
    font-family: "Cinzel", serif; font-weight: 600; font-size: 7.4px;
    letter-spacing: 0.2px;
  }
</style>
</head>
<body>

<section class="card card-front">
  <div class="front-brand">
    <div class="front-brand-circle"></div>
    <p class="front-brand-name">BKT Consulting</p>
  </div>
  <div class="divider"></div>
  <div class="contact">
    <h1 class="contact-name">Dana Velmonte</h1>
    <p class="contact-title">Principal</p>
    <ul class="contact-lines">
      <li>
        <svg width="12" height="12" viewBox="0 0 24 24"><path fill="#fff" d="M6.6 10.8a15.2 15.2 0 0 0 6.6 6.6l2.2-2.2a1 1 0 0 1 1-.25 11.4 11.4 0 0 0 3.6.57 1 1 0 0 1 1 1V20a1 1 0 0 1-1 1A17 17 0 0 1 3 4a1 1 0 0 1 1-1h3.5a1 1 0 0 1 1 1c0 1.25.2 2.45.57 3.57a1 1 0 0 1-.25 1z"/></svg>
        714 555-0186
      </li>
      <li>
        <svg width="12" height="10" viewBox="0 0 24 18"><path fill="#fff" d="M0 0h24v18H0z"/><path fill="none" stroke="#000" stroke-width="2" d="M1 1l11 9 11-9M1 17l8-7M23 17l-8-7"/></svg>
        dana.velmonte@mailbox.com
      </li>
      <li>DRE #05517382</li>
    </ul>
  </div>
  <p class="address">418 Larkspur Lane, Suite B, CA 92618</p>
</section>

<section class="card card-back">
  <div class="back-circle"></div>
  <h2 class="brand-name">BKT CONSULTING</h2>
  <p class="tagline">Real Estate/Government Liaison/ Public Outreach/ Entitlement Services</p>
</section>

</body>
</html>
```